Borin's Yard

I need a Bussiness Card for my new company in Miami Beach, my company is based in Winwood Miami and all around me is arts soo I would like my card with stripes, art design.

Target Market(s)

Artists, Actress, actors, show bussiness

Industry/Entity Type

It Company

Requirements
Must have
• Art Design

```html
<!DOCTYPE html>
<html lang="en">
<head>
<meta charset="utf-8">
<title>Borin's Yard — Business Card</title>
<link href="https://fonts.googleapis.com/css2?family=Play:wght@400;700&display=swap" rel="stylesheet">
<style>
  :root {
    --page-bg: #e9e6e2;
    --card-white: #ffffff;
    --card-shade: #ededed;
    --brand-red: #c1272d;
    --brand-deep: #8e1b20;
    --ink: #2b2b2b;
    --icon: #b3242a;
  }
  html, body {
    margin: 0;
    width: 1200px;
    height: 901px;
    overflow: hidden;
    background: var(--page-bg);
    font-family: "Play", sans-serif;
  }
  .business-card {
    position: absolute;
    left: 100px;
    top: 165px;
    width: 1000px;
    height: 572px;
    border-radius: 44px;
    overflow: hidden;
    background: radial-gradient(ellipse at 60% 55%, var(--card-white) 40%, var(--card-shade) 100%);
    box-shadow: 0 18px 40px rgba(0,0,0,0.18);
  }
  .header-band {
    position: absolute;
    inset: 0 0 auto 0;
    width: 1000px;
    height: 260px;
  }
  .holder {
    position: absolute;
    left: 150px;
    top: 38px;
    color: #fff;
  }
  .holder-name {
    margin: 0;
    font-size: 34px;
    font-weight: 400;
    letter-spacing: 0.5px;
  }
  .holder-role {
    margin: 4px 0 0 54px;
    font-size: 24px;
    font-style: italic;
  }
  .contact-list {
    position: absolute;
    left: 52px;
    top: 300px;
    margin: 0;
    padding: 0;
    list-style: none;
    color: var(--ink);
    font-size: 23px;
    letter-spacing: 0.6px;
  }
  .contact-list li {
    display: flex;
    align-items: center;
    gap: 12px;
    height: 38px;
  }
  .contact-list svg {
    width: 22px;
    height: 22px;
    fill: var(--icon);
    flex: none;
  }
  .brand-mark {
    position: absolute;
    right: 118px;
    top: 378px;
    display: flex;
    align-items: center;
    gap: 12px;
  }
  .brand-dot {
    width: 26px;
    height: 26px;
    border-radius: 50%;
    background: var(--brand-red);
  }
  .brand-name {
    font-size: 44px;
    font-weight: 700;
    color: var(--brand-red);
  }
  .address {
    position: absolute;
    right: 80px;
    top: 480px;
    margin: 0;
    font-style: normal;
    font-size: 24px;
    line-height: 34px;
    color: var(--ink);
    letter-spacing: 0.6px;
  }
</style>
</head>
<body>
  <section class="business-card">
    <svg class="header-band" viewBox="0 0 1000 260" aria-hidden="true">
      <path d="M0,0 H1000 V210 Q500,150 0,190 Z" fill="var(--brand-red)"/>
      <path d="M0,204 Q500,164 1000,224 L1000,232 Q500,174 0,212 Z" fill="var(--brand-deep)"/>
    </svg>

    <header class="holder">
      <h1 class="holder-name">Marlo Quince-Hart</h1>
      <p class="holder-role">consultant</p>
    </header>

    <ul class="contact-list">
      <li><svg viewBox="0 0 24 24"><path d="M6.6 10.8a15 15 0 0 0 6.6 6.6l2.2-2.2c.3-.3.7-.4 1-.2 1.1.4 2.3.6 3.6.6.6 0 1 .4 1 1V20c0 .6-.4 1-1 1A17 17 0 0 1 3 4c0-.6.4-1 1-1h3.5c.6 0 1 .4 1 1 0 1.3.2 2.5.6 3.6.1.3 0 .7-.2 1z"/></svg>014 280 3391</li>
      <li><svg viewBox="0 0 24 24"><path d="M7 1h10a2 2 0 0 1 2 2v18a2 2 0 0 1-2 2H7a2 2 0 0 1-2-2V3a2 2 0 0 1 2-2zm0 3v14h10V4zm5 15.2a1.2 1.2 0 1 0 0 2.4 1.2 1.2 0 0 0 0-2.4z"/></svg>014 280 3391</li>
      <li><svg viewBox="0 0 24 24"><path d="M6 2h9l3 3v5h2a2 2 0 0 1 2 2v10H2V12a2 2 0 0 1 2-2h2zm2 2v6h8V6h-3V4zm-2 10v2h2v-2zm4 0v2h2v-2zm4 0v2h2v-2z"/></svg>014 280 3391</li>
      <li><svg viewBox="0 0 24 24"><path d="M2 5h20v14H2zm2 2v.5l8 5.5 8-5.5V7z"/></svg>hello@borinsyard.com</li>
      <li><svg viewBox="0 0 24 24"><path d="M12 2a10 10 0 1 0 0 20 10 10 0 0 0 0-20zm6.9 6h-2.9a15 15 0 0 0-1.3-3.9A8 8 0 0 1 18.9 8zM12 4c.8 1.2 1.5 2.5 1.9 4h-3.8c.4-1.5 1.1-2.8 1.9-4zM4.3 14a8 8 0 0 1 0-4h3.3a16 16 0 0 0 0 4zm.8 2h2.9c.3 1.4.8 2.7 1.3 3.9A8 8 0 0 1 5.1 16zM8 8H5.1a8 8 0 0 1 4.2-3.9C8.8 5.3 8.3 6.6 8 8zm4 12c-.8-1.2-1.5-2.5-1.9-4h3.8c-.4 1.5-1.1 2.8-1.9 4zm2.3-6H9.7a14 14 0 0 1 0-4h4.6a14 14 0 0 1 0 4zm.4 5.9c.5-1.2 1-2.5 1.3-3.9h2.9a8 8 0 0 1-4.2 3.9zM16.4 14a16 16 0 0 0 0-4h3.3a8 8 0 0 1 0 4z"/></svg>www.borinsyard.com</li>
    </ul>

    <div class="brand-mark">
      <span class="brand-dot"></span>
      <span class="brand-name">Borin's Yard</span>
    </div>

    <address class="address">27,4th floor,Gallery<br>Lane Road NWK</address>
  </section>
</body>
</html>
```